Illustration of Healthcare Costs and comparison to alternative health insurance products

Create a data presentation template that allows our staff to modify it using photoshop. The design should be "clean" and "smart" without looking too "accounting/excel" like.

The graphic goes on the cover sheet of a proposal and allows the presenter to start the conversation with "here's what you were paying with product A, Here's Product B, and here's what you pay with our products.

A mock-up of the front page is attached.

Target Market(s)

Group Heath Insurance Buyer within a company - includes CEO, CFO and HR

Industry/Entity Type

Doctor

Font styles to use
Sans Serif
Other font styles liked:
• Calibri

Requirements
Must have
• Ability to easily modify all elements using Photoshop
Nice to have
• Ability to modify all elements using Powerpoint
Should not have
• Flat File we cannot modify

```html
<!DOCTYPE html>
<html lang="en">
<head>
<meta charset="utf-8">
<title>Annual Cost Comparison</title>
<link href="https://fonts.googleapis.com/css2?family=Carlito:wght@400;700&display=swap" rel="stylesheet">
<style>
  :root {
    --bg: #e6e2df;
    --axis: #4472c4;
    --bar-blue: #00bff0;
    --bar-green: #96e264;
    --teal: #006e6e;
    --taupe: #7a6e67;
    --orange: #f7931e;
    --red: #f0221e;
    --forest: #3a7a22;
    --white: #ffffff;
  }
  html, body {
    margin: 0;
    padding: 0;
    width: 1200px;
    height: 714px;
    overflow: hidden;
    background: var(--bg);
  }
  .chart {
    display: block;
    width: 1200px;
    height: 714px;
    font-family: "Carlito", Calibri, "Segoe UI", sans-serif;
  }
  .axis { fill: var(--axis); }
  .axis-title { fill: var(--axis); font-size: 31px; font-weight: 700; }
  .bar-base { fill: var(--bar-blue); }
  .bar-plan { fill: var(--bar-green); }
  .bar-cap { fill: var(--white); }
  .value-text { fill: var(--white); font-size: 21px; font-weight: 700; }
  .year-text { fill: var(--white); font-size: 37px; font-weight: 700; }
  .brand-name { fill: var(--axis); font-size: 28px; font-weight: 700; }
  .brand-dot { fill: var(--axis); }
  .tone-teal { fill: var(--teal); }
  .tone-taupe { fill: var(--taupe); }
  .tone-orange { fill: var(--orange); }
  .tone-red { fill: var(--red); }
  .tone-forest { fill: var(--forest); }
  .marker-ring { fill: var(--white); }
</style>
</head>
<body>
<svg class="chart" viewBox="0 0 1200 714" xmlns="http://www.w3.org/2000/svg" role="img" aria-label="Annual cost comparison 2014 to 2017">
  <defs>
    <linearGradient id="bar-shadow" x1="0" y1="0" x2="1" y2="0">
      <stop offset="0" stop-color="#b3aca7"/>
      <stop offset="1" stop-color="#e6e2df" stop-opacity="0"/>
    </linearGradient>
  </defs>

  <text class="axis-title" transform="translate(259 353) rotate(-90)" text-anchor="middle">Annual Cost</text>

  <g class="bar-shadows">
    <rect x="420" y="374" width="26" height="172" fill="url(#bar-shadow)"/>
    <rect x="582" y="310" width="26" height="236" fill="url(#bar-shadow)"/>
    <rect x="742" y="210" width="26" height="336" fill="url(#bar-shadow)"/>
    <rect x="904" y="162" width="26" height="384" fill="url(#bar-shadow)"/>
  </g>

  <g class="bar bar-2014">
    <rect class="bar-base" x="304" y="374" width="116" height="172"/>
    <rect class="bar-cap" x="304" y="372" width="116" height="5"/>
  </g>
  <g class="bar bar-2015">
    <rect class="bar-base" x="466" y="310" width="116" height="236"/>
    <rect class="bar-cap" x="466" y="308" width="116" height="5"/>
  </g>
  <g class="bar bar-2016">
    <rect class="bar-base" x="626" y="210" width="116" height="336"/>
    <rect class="bar-plan" x="626" y="256" width="116" height="290"/>
    <rect class="bar-cap" x="626" y="208" width="116" height="5"/>
    <rect class="bar-cap" x="626" y="254" width="116" height="5"/>
  </g>
  <g class="bar bar-2017">
    <rect class="bar-base" x="787" y="162" width="117" height="384"/>
    <rect class="bar-plan" x="787" y="257" width="117" height="289"/>
    <rect class="bar-cap" x="787" y="160" width="117" height="5"/>
    <rect class="bar-cap" x="787" y="255" width="117" height="5"/>
  </g>

  <g class="brand brand-2016">
    <circle class="brand-dot" cx="726" cy="372" r="3.5"/>
    <text class="brand-name" x="682" y="404" text-anchor="middle">Nobrivo</text>
  </g>
  <g class="brand brand-2017">
    <circle class="brand-dot" cx="888" cy="375" r="3.5"/>
    <text class="brand-name" x="844" y="407" text-anchor="middle">Nobrivo</text>
  </g>

  <rect class="axis" x="278" y="158" width="4" height="393"/>
  <rect class="axis" x="278" y="547" width="686" height="4"/>

  <g class="callout callout-2014">
    <rect class="tone-teal" x="305" y="310" width="117" height="40"/>
    <polygon class="tone-teal" points="356,349 376,349 364,362"/>
    <text class="value-text" x="363.5" y="337" text-anchor="middle">$ 4,000,000</text>
    <circle class="marker-ring" cx="360" cy="374" r="12"/>
    <circle class="tone-teal" cx="360" cy="374" r="7"/>
  </g>

  <g class="callout callout-2015">
    <rect class="tone-taupe" x="466" y="247" width="116" height="40"/>
    <polygon class="tone-taupe" points="516,286 536,286 524,299"/>
    <text class="value-text" x="524" y="274" text-anchor="middle">$ 4,520,000</text>
    <circle class="marker-ring" cx="521" cy="312" r="12"/>
    <circle class="tone-taupe" cx="521" cy="312" r="7"/>
  </g>

  <g class="callout callout-2016-top">
    <rect class="tone-orange" x="646" y="149" width="117" height="40"/>
    <polygon class="tone-orange" points="697,188 717,188 705,201"/>
    <text class="value-text" x="704.5" y="176" text-anchor="middle">$ 5,107,600</text>
    <circle class="marker-ring" cx="702" cy="213" r="12"/>
    <circle class="tone-orange" cx="702" cy="213" r="7"/>
  </g>

  <g class="callout callout-2016-plan">
    <rect class="tone-forest" x="606" y="286" width="116" height="40"/>
    <polygon class="tone-forest" points="655,287 675,287 662,272"/>
    <text class="value-text" x="664" y="313" text-anchor="middle">$ 5,100,600</text>
    <circle class="marker-ring" cx="662" cy="258" r="12"/>
    <circle class="tone-forest" cx="662" cy="258" r="7"/>
  </g>

  <g class="callout callout-2017-top">
    <rect class="tone-red" x="822" y="98" width="117" height="40"/>
    <polygon class="tone-red" points="872,137 892,137 880,150"/>
    <text class="value-text" x="880.5" y="125" text-anchor="middle">$ 5,107,600</text>
    <circle class="marker-ring" cx="877" cy="162" r="12"/>
    <circle class="tone-red" cx="877" cy="162" r="7"/>
  </g>

  <g class="callout callout-2017-plan">
    <rect class="tone-forest" x="774" y="287" width="116" height="40"/>
    <polygon class="tone-forest" points="822,288 842,288 829,273"/>
    <text class="value-text" x="832" y="314" text-anchor="middle">$ 5,100,600</text>
    <circle class="marker-ring" cx="829" cy="258" r="12"/>
    <circle class="tone-forest" cx="829" cy="258" r="7"/>
  </g>

  <g class="year-labels">
    <rect class="tone-teal" x="303" y="565" width="116" height="51"/>
    <text class="year-text" x="361" y="604" text-anchor="middle">2014</text>

    <rect class="tone-taupe" x="466" y="566" width="116" height="51"/>
    <text class="year-text" x="524" y="605" text-anchor="middle">2015</text>

    <rect class="tone-orange" x="626" y="566" width="116" height="51"/>
    <text class="year-text" x="684" y="605" text-anchor="middle">2016</text>

    <polygon class="tone-red" points="791,565 908,565 928,591 908,617 791,617"/>
    <text class="year-text" x="850" y="604" text-anchor="middle">2017</text>
  </g>
</svg>
</body>
</html>
```